PTA Business Card

Seeking design for a business card, standard size. It is going to be for myself in regards to PTA - details:

Hollis Brantley Elementary School
PTA President
Peter Lund
563-555-0147
Lundy1984@mailbarn.example

Requirement:
Facebook icon? "Hollis Brantley PTA Rusk"
Twitter thing? I am new to twitter so not sure what to put, here is the link:
https://twitter.example/HBRoversPTA

I was thinking on the front would be a notebook paper background? Not a requirement but was thinking it would look cool?

Total freedom here, let your creativity spread because I don't have any suggestions for design, sorry. Colors of school district are black and yellow.

Backside I am not sure exactly what to put on it.

```html
<!DOCTYPE html>
<html lang="en">
<head>
<meta charset="utf-8">
<title>Hollis Brantley PTA – Business Card</title>
<link href="https://fonts.googleapis.com/css2?family=Indie+Flower&display=swap" rel="stylesheet">
<style>
  :root {
    --backdrop: #e7e5e1;
    --paper: #fcfbf1;
    --paper-edge: #f6f2d8;
    --grid: rgba(120, 140, 210, 0.28);
    --margin-rule: rgba(226, 120, 140, 0.7);
    --ink: #2c52a6;
    --doodle-fill: rgba(44, 82, 166, 0.1);
  }
  * { box-sizing: border-box; margin: 0; padding: 0; }
  html, body {
    width: 1200px; height: 918px; overflow: hidden;
    background: var(--backdrop);
  }
  .canvas {
    position: relative; width: 1200px; height: 918px;
    display: flex; flex-direction: column; align-items: center; justify-content: center;
    gap: 38px;
  }
  .card {
    position: relative; width: 700px; height: 400px;
    background-color: var(--paper);
    background-image:
      radial-gradient(ellipse at 80% 20%, var(--paper) 0%, var(--paper-edge) 100%),
      linear-gradient(var(--grid) 1px, transparent 1px),
      linear-gradient(90deg, var(--grid) 1px, transparent 1px);
    background-blend-mode: multiply;
    background-size: 100% 100%, 24px 24px, 24px 24px;
    box-shadow: 0 6px 18px rgba(0, 0, 0, 0.15);
    font-family: "Indie Flower", cursive;
    color: var(--ink);
    overflow: hidden;
  }
  .doodle {
    position: absolute; background: var(--doodle-fill); border-radius: 6px;
  }

  /* Contact side */
  .contact .identity { position: absolute; left: 120px; top: 34px; }
  .contact .name {
    font-size: 40px; letter-spacing: 1px; line-height: 1; font-weight: 400;
  }
  .contact .role { font-size: 24px; line-height: 1.1; margin-left: 4px; font-weight: 400; }
  .contact .details {
    position: absolute; left: 80px; top: 140px; list-style: none;
    font-size: 24px; line-height: 40px;
  }
  .contact .details li { display: flex; align-items: center; gap: 14px; white-space: nowrap; }
  .contact .details svg { width: 24px; height: 24px; flex: none; }

  /* School side */
  .school .margin-rule {
    position: absolute; left: 46px; top: 0; bottom: 0; width: 2px;
    background: var(--margin-rule);
  }
  .school .school-name {
    position: absolute; left: 64px; right: 20px; top: 172px;
    font-size: 42px; line-height: 1; font-weight: 400;
    text-align: center; white-space: nowrap;
  }
</style>
</head>
<body>
<main class="canvas">

  <section class="card contact" aria-label="Card front: contact details">
    <div class="identity">
      <h1 class="name">PETER LUND</h1>
      <p class="role">PTA President</p>
    </div>
    <ul class="details">
      <li>
        <svg viewBox="0 0 24 24" aria-hidden="true"><rect x="6" y="2" width="12" height="20" rx="2" fill="none" stroke="currentColor" stroke-width="2"/><line x1="10" y1="18" x2="14" y2="18" stroke="currentColor" stroke-width="2"/></svg>
        <span>563-555-0147</span>
      </li>
      <li>
        <svg viewBox="0 0 24 24" aria-hidden="true"><rect x="2" y="5" width="20" height="14" rx="2" fill="none" stroke="currentColor" stroke-width="2"/><polyline points="2,6 12,13 22,6" fill="none" stroke="currentColor" stroke-width="2"/></svg>
        <span>Lundy1984@mailbarn.example</span>
      </li>
      <li>
        <svg viewBox="0 0 24 24" aria-hidden="true"><circle cx="12" cy="12" r="10" fill="currentColor"/></svg>
        <span>&lt;Hollis Brantley PTA Rusk&gt;</span>
      </li>
      <li>
        <svg viewBox="0 0 24 24" aria-hidden="true"><circle cx="12" cy="12" r="10" fill="currentColor"/></svg>
        <span>&lt;HBRoversPTA&gt;</span>
      </li>
    </ul>
    <div class="doodle" role="img" aria-label="Pen doodles of a smiling sun and a small heart" style="left:560px; top:230px; width:110px; height:50px;"></div>
    <div class="doodle" role="img" aria-label="Pen doodle of a stick figure" style="left:545px; top:300px; width:60px; height:55px;"></div>
    <div class="doodle" role="img" aria-label="Pen doodles of a triangle, a circle and stars" style="left:440px; top:330px; width:100px; height:50px;"></div>
  </section>

  <section class="card school" aria-label="Card back: school name">
    <div class="margin-rule"></div>
    <div class="doodle" role="img" aria-label="Pen doodle of a closed book with a star" style="left:64px; top:30px; width:150px; height:90px;"></div>
    <div class="doodle" role="img" aria-label="Pen doodles of a smiling sun and a heart" style="left:590px; top:60px; width:80px; height:90px;"></div>
    <h2 class="school-name">Hollis Brantley Elementary School</h2>
    <div class="doodle" role="img" aria-label="Pen doodle of a stick figure with a star" style="left:70px; top:265px; width:100px; height:70px;"></div>
    <div class="doodle" role="img" aria-label="Pen doodles of an apple and a school satchel" style="left:470px; top:280px; width:180px; height:95px;"></div>
  </section>

</main>
</body>
</html>
```